Presentation Folder

We are looking for a presentation folder design that will allow us to bring our proposals/quotes to clients and leave with them. The front cover should have our logo as well as show some of the products we sell: IT Networking equipment, WiFi, Servers/Storage.
Inside flap has an area for our business cards.

Target Market(s)

Mid Sized Businesses and Private Education. Business to Business. IT Directors. Ages 30 to 50. College Educated. Southern California

Industry/Entity Type

Business

Logo Text

Requirements
Must have
• Our Logo
Complimentary color schemes to our logo.
Should be Professional.

```html
<!DOCTYPE html>
<html lang="en">
<head>
<meta charset="utf-8">
<title>Halverntech Presentation Folder</title>
<link href="https://fonts.googleapis.com/css2?family=Questrial&family=Cinzel:wght@400;600&display=swap" rel="stylesheet">
<style>
  :root {
    --stage: #ececec;
    --cover-grey: #939598;
    --brand-blue: #00b0da;
    --band-grey: #98999c;
    --paper: #ffffff;
    --paper-shade: #ececed;
    --ink-grey: #8d8f92;
    --ink-dark: #3a3b3d;
    --white: #ffffff;
  }
  * { margin: 0; padding: 0; box-sizing: border-box; }
  html, body { width: 1200px; height: 1105px; overflow: hidden; }
  body { background: var(--stage); position: relative; font-family: "Questrial", sans-serif; }

  .folder { position: absolute; left: 17px; top: 25px; width: 1166px; height: 1054px; }

  .back-cover {
    position: absolute; left: 0; top: 0; width: 584px; height: 778px;
    background: var(--cover-grey); color: var(--white);
  }
  .back-cover .wordmark {
    position: absolute; left: 0; width: 584px; top: 340px;
    text-align: center; font-size: 63px; letter-spacing: 1px; line-height: 1;
  }
  .back-cover .contact {
    position: absolute; left: 0; width: 584px; top: 723px;
    text-align: center; font-size: 15px; line-height: 19px; letter-spacing: 0.2px;
  }

  .pocket { position: absolute; left: 0; top: 778px; width: 584px; height: 276px; }

  .front-cover {
    position: absolute; left: 584px; top: 0; width: 582px; height: 778px;
    background: linear-gradient(to bottom, var(--paper) 0, var(--paper) 520px, #f6f6f7 560px, var(--paper-shade) 778px);
    overflow: hidden;
  }
  .product-visual {
    position: absolute; left: 15px; top: 57px; width: 549px; height: 360px;
    background: radial-gradient(ellipse at 50% 55%, #cfe9f2 0%, #e7eef2 45%, var(--paper) 75%);
  }
  .ribbons { position: absolute; left: 0; top: 472px; width: 582px; height: 56px; }
  .tagline {
    position: absolute; font-family: "Cinzel", serif; color: var(--white); line-height: 1;
  }
  .tagline.lead { left: 22px; top: 480px; font-size: 23px; font-weight: 600; }
  .tagline.follow { left: 285px; top: 500px; font-size: 19px; }
  .front-cover .wordmark {
    position: absolute; left: 0; width: 582px; top: 622px;
    text-align: center; font-size: 63px; color: var(--ink-grey); letter-spacing: 1px; line-height: 1;
  }
  .product-list {
    position: absolute; left: 0; width: 558px; top: 739px;
    text-align: center; font-size: 19px; color: var(--ink-dark);
  }
</style>
</head>
<body>
  <div class="folder">
    <section class="back-cover">
      <div class="wordmark">HALVERNTECH</div>
      <div class="contact">
        <p>p : +12 345 67890 &nbsp;|&nbsp; f : +12 345 67890 &nbsp;|&nbsp; e : info@website.com</p>
        <p>w : www.halverntech.com &nbsp;|&nbsp; #0000, Street Name, Area Name, Country Code</p>
      </div>
    </section>

    <svg class="pocket" viewBox="0 0 584 276" aria-hidden="true">
      <polygon points="0,0 584,0 476,276 0,276" fill="var(--brand-blue)"/>
      <line x1="92" y1="54" x2="184" y2="21" stroke="#1d2a30" stroke-width="1.2"/>
      <line x1="346" y1="247" x2="437" y2="215" stroke="#1d2a30" stroke-width="1.2"/>
    </svg>

    <section class="front-cover">
      <div class="product-visual" role="img" aria-label="Illustration of server racks connected by arrows to several laptops showing world maps"></div>
      <svg class="ribbons" viewBox="0 0 582 56" aria-hidden="true">
        <polygon points="168,54 186,18 582,18 582,54" fill="var(--band-grey)"/>
        <polygon points="0,0 285,0 253,36 0,36" fill="var(--brand-blue)"/>
      </svg>
      <div class="tagline lead">Get Connected</div>
      <div class="tagline follow">Anywhere, Anytime</div>
      <div class="wordmark">HALVERNTECH</div>
      <p class="product-list">&bull; IT Networking equipment &bull; WiFi &bull; Servers/Storage</p>
    </section>
  </div>
</body>
</html>
```